Graphic to show easy steps to find financial clarity

Howdy-I need a graphic that describe my Coin Harbor Method.The attached is a concept, but please use your own creativity to show how you would display this:- There are 5 steps the process (and then we repeat/recalculate)- And three bullets that drive home the results of the processI've also attached my logo. Please use the colors in my logo and maybe add a soft green as needed.The reader should be able to briefly scan this document and understand that this is an easy/simple process that tells them how to manage their cash.Thanks!-Ned

Target Market(s)

wealthy women, whether single or married

Requirements
Must have
• Please use the colors in my logo and a soft green if needed
Should not have
• This should be a very easy to read graphic that communicates how simple/easy this is to do.

```html
<!DOCTYPE html>
<html lang="en">
<head>
<meta charset="utf-8">
<title>Coin Harbor Method</title>
<link rel="stylesheet" href="https://fonts.googleapis.com/css2?family=Montserrat:wght@600&family=Open+Sans:wght@400;500&display=swap">
<style>
  :root {
    --navy: #0b3a7e;
    --green: #77bb78;
    --green-light: #98d896;
    --pill-grey: #666666;
    --line-grey: #666666;
    --bg-center: #ffffff;
    --bg-edge: #e4e4e4;
    --white: #ffffff;
  }
  html, body { margin: 0; padding: 0; overflow: hidden; }
  .canvas {
    position: relative;
    width: 1200px;
    height: 889px;
    overflow: hidden;
    background: radial-gradient(ellipse at 50% 50%, var(--bg-center) 0%, #f4f4f4 45%, var(--bg-edge) 100%);
    font-family: "Open Sans", Arial, sans-serif;
  }
  .title {
    position: absolute;
    top: 34px; left: 0; width: 1200px;
    margin: 0;
    text-align: center;
    font-family: "Montserrat", Arial, sans-serif;
    font-weight: 600;
    font-size: 44px;
    letter-spacing: 6px;
    color: var(--navy);
    text-transform: uppercase;
  }
  .diagram { position: absolute; top: 0; left: 0; }
  .step-label {
    position: absolute;
    display: flex; align-items: center; justify-content: center;
    height: 63px;
    border-radius: 32px;
    background: var(--green);
    color: var(--white);
    font-size: 19px;
    line-height: 23px;
    text-align: center;
    text-transform: uppercase;
    box-shadow: 0 2px 3px rgba(0,0,0,0.12);
  }
  .step-label.upper { top: 119px; }
  .step-label.lower { top: 208px; }
  .result {
    position: absolute;
    display: flex; align-items: center; justify-content: center;
    height: 38px;
    border-radius: 19px;
    background: var(--pill-grey);
    color: var(--white);
    font-size: 20px;
    text-transform: uppercase;
    white-space: nowrap;
  }
</style>
</head>
<body>
<div class="canvas">
  <h1 class="title">Coin Harbor Method</h1>

  <svg class="diagram" width="1200" height="889" viewBox="0 0 1200 889" aria-hidden="true">
    <defs>
      <linearGradient id="hexFrame" x1="0" y1="0" x2="0" y2="1">
        <stop offset="0" stop-color="#98d896"/>
        <stop offset="0.45" stop-color="#79b98f"/>
        <stop offset="0.75" stop-color="#1e5689"/>
        <stop offset="1" stop-color="#0b3a7e"/>
      </linearGradient>
      <marker id="greenHead" markerWidth="10" markerHeight="10" refX="5" refY="8" orient="auto" markerUnits="userSpaceOnUse">
        <path d="M0,0 L5,9 L10,0 L5,4 Z" fill="#77bb78"/>
      </marker>
      <g id="hex">
        <path d="M-84,0 L-44,-74 L44,-74 L84,0 L44,74 L-44,74 Z" fill="var(--white)" stroke="url(#hexFrame)" stroke-width="18" stroke-linejoin="round"/>
      </g>
    </defs>

    <!-- connectors from labels -->
    <g class="connectors" stroke="#77bb78" stroke-width="2" marker-end="url(#greenHead)">
      <line x1="170" y1="271" x2="170" y2="330"/>
      <line x1="336" y1="182" x2="336" y2="330"/>
      <line x1="498" y1="271" x2="498" y2="330"/>
      <line x1="666" y1="182" x2="666" y2="330"/>
      <line x1="829" y1="271" x2="829" y2="330"/>
      <line x1="996" y1="182" x2="996" y2="330"/>
    </g>

    <!-- hexagon chain -->
    <g class="hex-chain">
      <use href="#hex" x="170" y="411"/>
      <use href="#hex" x="336" y="411"/>
      <use href="#hex" x="498" y="411"/>
      <use href="#hex" x="666" y="411"/>
      <use href="#hex" x="829" y="411"/>
      <use href="#hex" x="996" y="411"/>
    </g>

    <!-- icons -->
    <g class="icons" fill="var(--navy)" stroke="var(--navy)">
      <!-- cash with up/down arrows -->
      <g transform="translate(170,411)">
        <rect x="-26" y="-18" width="52" height="30" rx="2" fill="none" stroke-width="4" transform="rotate(8)"/>
        <rect x="-30" y="-24" width="52" height="30" rx="2" stroke="none" transform="rotate(8)"/>
        <text x="-6" y="-1" font-size="22" font-weight="700" fill="#fff" stroke="none" text-anchor="middle" font-family="Arial, sans-serif" transform="rotate(8)">$</text>
        <path d="M-14,-40 L-24,-30 M-14,-40 L-4,-30 M-14,-40 L-14,-26" fill="none" stroke-width="5" stroke-linecap="round"/>
        <path d="M22,30 L12,20 M22,30 L32,20 M22,30 L22,16" fill="none" stroke-width="5" stroke-linecap="round"/>
      </g>
      <!-- wallet -->
      <g transform="translate(336,411)">
        <path d="M-34,-10 L28,-26 L34,-18" fill="none" stroke-width="4"/>
        <rect x="-36" y="-12" width="70" height="38" rx="2" fill="none" stroke-width="5"/>
        <line x1="-28" y1="2" x2="26" y2="2" stroke-width="3"/>
        <rect x="8" y="-34" width="22" height="16" rx="2" stroke="none" transform="rotate(-30 19 -26)"/>
      </g>
      <!-- calendar with cash -->
      <g transform="translate(498,411)">
        <rect x="-32" y="-28" width="64" height="60" rx="5" fill="none" stroke-width="5"/>
        <rect x="-32" y="-28" width="64" height="12" stroke="none"/>
        <line x1="-16" y1="-38" x2="-16" y2="-24" stroke-width="5" stroke-linecap="round"/>
        <line x1="16" y1="-38" x2="16" y2="-24" stroke-width="5" stroke-linecap="round"/>
        <rect x="-18" y="-2" width="36" height="20" rx="2" fill="none" stroke-width="3" transform="rotate(12)"/>
        <circle cx="2" cy="10" r="6" stroke="none"/>
      </g>
      <!-- hand with coin -->
      <g transform="translate(666,411)">
        <circle cx="4" cy="-22" r="17" stroke="none"/>
        <text x="4" y="-14" font-size="22" font-weight="700" fill="#fff" stroke="none" text-anchor="middle" font-family="Arial, sans-serif">$</text>
        <rect x="-44" y="6" width="6" height="26" stroke="none"/>
        <path d="M-34,12 C-20,4 -6,6 4,14 L16,14 M-34,28 L4,28 L40,8" fill="none" stroke-width="5" stroke-linejoin="round" stroke-linecap="round"/>
      </g>
      <!-- plant with coin -->
      <g transform="translate(829,411)">
        <circle cx="6" cy="-28" r="13" stroke="none"/>
        <text x="6" y="-21" font-size="18" font-weight="700" fill="#fff" stroke="none" text-anchor="middle" font-family="Arial, sans-serif">$</text>
        <path d="M0,0 C-2,-6 0,-12 4,-16" fill="none" stroke-width="3"/>
        <path d="M-2,-6 C-10,-20 -26,-18 -28,-14 C-24,-6 -12,-2 -2,-6 Z" stroke="none"/>
        <path d="M4,-6 C12,-18 28,-16 30,-12 C24,-4 14,-2 4,-6 Z" stroke="none"/>
        <path d="M-22,4 L22,4 L16,34 L-16,34 Z" stroke="none"/>
      </g>
      <!-- document with pencil -->
      <g transform="translate(996,411)">
        <path d="M-26,-30 L22,-30 L22,26 L-30,26 L-30,-22 Z" fill="none" stroke-width="4" stroke-linejoin="round"/>
        <line x1="-10" y1="-18" x2="12" y2="-18" stroke-width="3"/>
        <line x1="-10" y1="-9" x2="12" y2="-9" stroke-width="3"/>
        <line x1="-20" y1="0" x2="4" y2="0" stroke-width="3"/>
        <line x1="-20" y1="9" x2="-2" y2="9" stroke-width="3"/>
        <path d="M4,30 L30,4 L36,10 L10,36 L2,38 Z" stroke="none"/>
      </g>
    </g>

    <!-- results bracket -->
    <g class="results-bracket" fill="none" stroke="var(--line-grey)" stroke-width="1.6">
      <polyline points="1089,411 1132,411 1132,754 1042,754"/>
      <line x1="1132" y1="624" x2="808" y2="624"/>
      <line x1="1132" y1="689" x2="924" y2="689"/>
    </g>
    <g class="results-arrows" fill="var(--line-grey)">
      <path d="M1132,544 L1125,528 L1132,532 L1139,528 Z"/>
      <path d="M964,624 L980,617 L976,624 L980,631 Z"/>
      <path d="M1028,689 L1044,682 L1040,689 L1044,696 Z"/>
      <path d="M1064,754 L1080,747 L1076,754 L1080,761 Z"/>
    </g>
  </svg>

  <div class="step-label lower" style="left:57px; width:225px;">Know your<br>annual spending</div>
  <div class="step-label upper" style="left:232px; width:193px;">Project simple<br>expenses</div>
  <div class="step-label lower" style="left:391px; width:216px;">Add up your 5<br>year cash needs</div>
  <div class="step-label upper" style="left:570px; width:191px;">Set them aside<br>in savings</div>
  <div class="step-label lower" style="left:769px; width:135px;">Invest<br>the rest</div>
  <div class="step-label upper" style="left:910px; width:168px;">Recalculate<br>monthly</div>

  <div class="result" style="left:362px; top:606px; width:444px;">Spend intentionally and with joy</div>
  <div class="result" style="left:246px; top:670px; width:676px;">Create a sold base for lifetime cash flow projections</div>
  <div class="result" style="left:129px; top:735px; width:910px;">Know your lifestyle will be unaffected by the markets for atleast 5 years</div>
</div>
</body>
</html>
```